Business cards — need something that creates “wow” factor

Need a sleek and clean looking business card. Something that is clear and consise. These business cards are for my painting business and hundreds will be placed in the Dallas area between all Halverd Pemberton paint stored. These card really need to stick out! Open to any and all ideas...

Target Market(s)

Residential clientele

Industry/Entity Type

Painting

Contact Information for Business Card

Dorian Vakelby
Owner

382.516.2074

Web: Mesahuepainting.example (still under construction)
Mesahuepainting@mailbox.example

Font styles to use
Sans Serif

Colors

Designer to choose colors to be used in the design.

Requirements
Must have
• My name, number, website, email, Socialpage
• and “100% customer satisfaction guaranteed”
• Socialpage.example/Mesahuepainting/
Nice to have
• Listed services
• Interior/exterior painting
• Drywall repair/texture
• Fence staining/refinishing
• Concrete staining
• Epoxy flooring
• Pressure washing

```html
<!DOCTYPE html>
<html lang="en">
<head>
<meta charset="utf-8">
<title>Mesahue Painting — Business Card</title>
<link href="https://fonts.googleapis.com/css2?family=Roboto:wght@400;500;700&family=Roboto+Condensed:ital,wght@0,700;1,700&display=swap" rel="stylesheet">
<style>
  :root {
    --backdrop: #e6e6e4;
    --paper: #f7f7f6;
    --teal: #3890ae;
    --ink: #3f3f3f;
    --ink-dark: #1d1d1d;
    --white: #ffffff;
  }
  * { margin: 0; padding: 0; box-sizing: border-box; }
  html, body { width: 1200px; height: 960px; overflow: hidden; }
  body {
    position: relative;
    background: var(--backdrop);
    font-family: "Roboto", Arial, sans-serif;
  }
  .card {
    position: absolute;
    width: 600px;
    height: 343px;
    box-shadow: 0 2px 6px rgba(0,0,0,0.25);
  }
  .card--front { left: 314px; top: 113px; background: var(--paper); }
  .card--back  { left: 311px; top: 472px; background: var(--teal); }

  .wordmark {
    position: absolute;
    display: flex;
    align-items: center;
    gap: 10px;
    font-family: "Roboto", Arial, sans-serif;
    font-weight: 500;
    font-size: 30px;
    line-height: 1.05;
    letter-spacing: 1px;
  }
  .wordmark__mark { width: 16px; height: 16px; flex: none; }
  .card--front .wordmark { left: 44px; top: 92px; color: var(--ink-dark); }
  .card--front .wordmark__mark { background: var(--teal); }
  .card--back .wordmark { left: 80px; top: 117px; color: var(--white); }
  .card--back .wordmark__mark { background: var(--white); }

  .identity {
    position: absolute;
    right: 48px;
    top: 93px;
    text-align: right;
  }
  .identity__name {
    font-family: "Roboto Condensed", "Arial Narrow", sans-serif;
    font-weight: 700;
    font-size: 20px;
    color: var(--teal);
    letter-spacing: 0.2px;
  }
  .identity__role {
    font-size: 14px;
    font-weight: 500;
    color: var(--ink-dark);
    letter-spacing: 0.5px;
    margin-top: 1px;
  }

  .contacts {
    position: absolute;
    left: 44px;
    top: 207px;
    list-style: none;
  }
  .contacts__item {
    display: flex;
    align-items: center;
    height: 19px;
    font-size: 14.5px;
    color: var(--ink);
  }
  .contacts__icon { width: 13px; height: 13px; margin-right: 9px; flex: none; fill: var(--teal); }

  .guarantee {
    position: absolute;
    left: 0;
    top: 299px;
    width: 545px;
    height: 28px;
  }
  .guarantee svg { position: absolute; inset: 0; }
  .guarantee__text {
    position: absolute;
    left: 40px;
    top: 3px;
    font-family: "Roboto Condensed", "Arial Narrow", sans-serif;
    font-style: italic;
    font-weight: 700;
    font-size: 17px;
    color: var(--white);
  }

  .services {
    position: absolute;
    left: 307px;
    top: 106px;
    list-style: none;
  }
  .services__item {
    position: relative;
    padding-left: 13px;
    height: 23px;
    font-size: 14.5px;
    color: var(--white);
  }
  .services__item::before {
    content: "";
    position: absolute;
    left: 0;
    top: 7px;
    width: 5px;
    height: 5px;
    border-radius: 50%;
    background: var(--white);
  }
</style>
</head>
<body>
  <section class="card card--front">
    <div class="wordmark"><span class="wordmark__mark"></span><span>Mesahue<br>Painting</span></div>

    <div class="identity">
      <div class="identity__name">DORIAN VAKELBY</div>
      <div class="identity__role">OWNER</div>
    </div>

    <ul class="contacts">
      <li class="contacts__item">
        <svg class="contacts__icon" viewBox="0 0 16 16"><path d="M3.6 1.2l2.3 2.9-1.3 1.6c.9 2 2.5 3.6 4.5 4.6l1.6-1.3 2.9 2.3-1.2 2.2C7.2 13.7 2.4 8.9 1.4 3.3z"/></svg>
        382.516.2074
      </li>
      <li class="contacts__item">
        <svg class="contacts__icon" viewBox="0 0 16 16"><path d="M1 3h14v10H1z M2.5 4.5L8 8.7l5.5-4.2" fill="none" stroke="#3890ae" stroke-width="1.6"/><rect x="1" y="3" width="14" height="10" fill="#3890ae"/><path d="M1.5 3.6L8 8.5l6.5-4.9" fill="none" stroke="#f7f7f6" stroke-width="1.3"/></svg>
        Mesahuepainting@mailbox.example
      </li>
      <li class="contacts__item">
        <svg class="contacts__icon" viewBox="0 0 16 16"><circle cx="8" cy="8" r="7"/><path d="M1 8h14M8 1c-3 3.5-3 10.5 0 14M8 1c3 3.5 3 10.5 0 14" fill="none" stroke="#f7f7f6" stroke-width="1.1"/></svg>
        Mesahuepainting.example
      </li>
      <li class="contacts__item">
        <svg class="contacts__icon" viewBox="0 0 16 16"><rect x="1" y="1" width="14" height="14" rx="1.5"/></svg>
        Mesahuepainting
      </li>
    </ul>

    <div class="guarantee">
      <svg viewBox="0 0 545 28" width="545" height="28" preserveAspectRatio="none">
        <path d="M0 0H530l4 1 -2 3 8 1 -3 4 5 2 -4 4 6 2 -5 3 4 3 -6 2 3 2H0z" fill="#3890ae"/>
      </svg>
      <span class="guarantee__text">100% customer satisfaction guaranteed</span>
    </div>
  </section>

  <section class="card card--back">
    <div class="wordmark"><span class="wordmark__mark"></span><span>Mesahue<br>Painting</span></div>

    <ul class="services">
      <li class="services__item">Interior/exterior painting</li>
      <li class="services__item">Drywall repair/texture</li>
      <li class="services__item">Fence staining/refinishing</li>
      <li class="services__item">Concrete staining</li>
      <li class="services__item">Epoxy flooring</li>
      <li class="services__item">Pressure washing</li>
    </ul>
  </section>
</body>
</html>
```